Design for an annual report

Take our current design of our annual report and spice it up to make it look more professional. We are a private equity company investing in industrial companies, so we need something clean, professional, modern and stylish. Nothing B2C but very professional looking design.

- Redo the cover page
- Redo the tables and charts
- Change the font
- add a few pictures (front page picture can be changed). Stay with industrial pictures (see www.velnor-ag.ch) or swiss alps pictures.

Stay with grey, blue colors. not to many colors.

only work on it if you have real experience in designing annual repots for corporations.

Target Market(s)

financial investors in industrial companies. shareholders of our company.

most readers are 60+, Europeans, men.

Industry/Entity Type

Industrial

Font styles to use
Serif

Colors
85acd3
0455a3
eaf1f6
ceddec
c8c8c8
757575
1b1b1b
cfeae6

Requirements
Must have
• Very clean design and modern. not colorful, straight, clean, simple, professional.

See attached picture of the cover page of our corporate presentation. should use same color styles. doesnt have to be idential.
Should not have
• stay with blue shades and grey shades. Not too many colors.

```html
<!DOCTYPE html>
<html lang="de">
<head>
<meta charset="utf-8">
<title>Geschäftsbericht Velnor AG</title>
<link href="https://fonts.googleapis.com/css2?family=Cinzel:wght@400;700&family=Arimo:wght@400&display=swap" rel="stylesheet">
<style>
  :root{
    --backdrop:#e6e8eb;
    --page:#ffffff;
    --blue-deep:#0455a3;
    --blue-mid:#85acd3;
    --blue-ink:#1f3d86;
    --blue-title:#1d4f9c;
    --grey-mid:#757575;
    --grey-light:#c8c8c8;
    --ink:#1b1b1b;
    --panel:#eef0f2;
  }
  *{box-sizing:border-box;margin:0;padding:0}
  html,body{width:1200px;height:802px;overflow:hidden;background:var(--backdrop)}
  .spread{position:absolute;left:36px;top:36px;width:1128px;height:730px;display:flex;box-shadow:0 2px 8px rgba(0,0,0,.18)}
  .page{position:relative;width:564px;height:730px;overflow:hidden}
  .page--back{background:linear-gradient(#ffffff 45%,var(--panel))}
  .page--cover{background:var(--page)}
  .page svg.art{position:absolute;left:0;top:0}
  .serif{font-family:"Cinzel",Georgia,serif}
  .sans{font-family:"Arimo",Arial,sans-serif}

  .contact-heading{position:absolute;left:12px;top:355px;font-size:22px;color:var(--blue-title);font-weight:700}
  .contact-intro{position:absolute;left:12px;top:389px;width:372px;font-size:12px;line-height:15px;color:var(--ink)}
  .person{position:absolute;top:441px;width:140px;text-align:center}
  .person__role{display:inline-block;background:var(--ink);color:#fff;font-size:9.5px;line-height:11px;padding:3px 7px;font-weight:700}
  .person__portrait{display:block;margin:7px auto 0;width:80px;height:120px;background:linear-gradient(#ececec,#8e8e8e)}
  .person__contact{margin-top:6px;font-size:8.5px;line-height:10px;color:var(--ink);font-weight:700}
  .divider{position:absolute;left:18px;top:638px;width:450px;height:1px;background:linear-gradient(90deg,var(--grey-light),transparent)}
  .company-heading{position:absolute;left:18px;top:644px;font-size:14px;color:var(--ink);font-weight:400}
  .brand{position:absolute;display:flex;align-items:center;gap:10px;color:var(--blue-ink);font-family:"Cinzel",Georgia,serif;font-weight:700}
  .brand__mark{width:14px;height:14px;background:var(--blue-ink)}
  .brand--footer{left:24px;top:672px;font-size:34px}
  .address{position:absolute;left:289px;top:664px;font-size:10px;line-height:14px;color:var(--ink);font-weight:700}
  .brand--cover{right:22px;top:20px;font-size:36px}

  .cover-title{position:absolute;left:0;width:564px;text-align:center;color:#fff}
  .cover-title--main{top:532px;font-size:27px;font-weight:400}
  .cover-title--year{top:598px;font-size:21px;font-weight:700}
  .cover-claim{position:absolute;left:0;top:658px;width:564px;text-align:center;font-size:15.5px;line-height:22px;color:#2a2f38}
</style>
</head>
<body>
<div class="spread">
  <section class="page page--back">
    <svg class="art" width="564" height="360" viewBox="0 0 564 360">
      <defs>
        <linearGradient id="alpPeak" x1="0" y1="0" x2="0.35" y2="1">
          <stop offset="0" stop-color="#0f4a8c"/>
          <stop offset=".22" stop-color="#2a609a"/>
          <stop offset=".38" stop-color="#5c6570"/>
          <stop offset=".52" stop-color="#8c939c"/>
          <stop offset=".7" stop-color="#d9dee4"/>
          <stop offset="1" stop-color="#f6f8fa"/>
        </linearGradient>
      </defs>
      <path d="M0 0H564V312Q280 372 0 282Z" fill="var(--grey-mid)"/>
      <path d="M0 0H564V286Q270 362 0 282Z" fill="var(--blue-mid)"/>
      <path role="img" aria-label="Foto: verschneiter Alpengipfel vor blauem Himmel" d="M0 0H564V260Q262 348 0 282Z" fill="url(#alpPeak)"/>
      <path d="M0 282Q262 348 564 260" fill="none" stroke="var(--blue-deep)" stroke-width="5"/>
    </svg>

    <h2 class="contact-heading serif">Kontaktinformationen</h2>
    <p class="contact-intro sans">Wenn Sie ein Foto durch ein eigenes ersetzen möchten, klicken Sie mit der rechten Maustaste darauf, und wählen Sie "Bild ändern" aus.</p>

    <div class="person serif" style="left:42px">
      <span class="person__role">Martin Hagedorn<br>Geschäftsführer</span>
      <span class="person__portrait" role="img" aria-label="Porträtfoto Martin Hagedorn"></span>
      <p class="person__contact">Tel.[Telefon]<br>[E-Mail-Adresse]</p>
    </div>
    <div class="person serif" style="left:223px">
      <span class="person__role">Stefan Brunold<br>Geschäftsführer</span>
      <span class="person__portrait" role="img" aria-label="Porträtfoto Stefan Brunold"></span>
      <p class="person__contact">Tel.[Telefon]<br>[E-Mail-Adresse]</p>
    </div>
    <div class="person serif" style="left:397px">
      <span class="person__role">Lukas Imhasly<br>Projekt Manager</span>
      <span class="person__portrait" role="img" aria-label="Porträtfoto Lukas Imhasly"></span>
      <p class="person__contact">Tel.[Telefon]<br>[E-Mail-Adresse]</p>
    </div>

    <div class="divider"></div>
    <h3 class="company-heading serif">Firmeninformationen</h3>
    <div class="brand brand--footer"><span class="brand__mark"></span>VELNOR</div>
    <p class="address serif">Seefeldweg 14, 8008 Zürich<br>Tel : 044 210 55 40<br>Fax : 044 210 55 41<br>Web : www.velnor-ag.ch</p>
  </section>

  <section class="page page--cover">
    <div class="brand brand--cover"><span class="brand__mark"></span>VELNOR</div>
    <svg class="art" width="564" height="730" viewBox="0 0 564 730">
      <defs>
        <linearGradient id="hazyRange" x1="0" y1="0" x2="0" y2="1">
          <stop offset="0" stop-color="#e6eaee"/>
          <stop offset=".38" stop-color="#d3dbe3"/>
          <stop offset=".55" stop-color="#9fb0c2"/>
          <stop offset=".72" stop-color="#5f738c"/>
          <stop offset=".86" stop-color="#3f5068"/>
          <stop offset="1" stop-color="#b9c5d3"/>
        </linearGradient>
      </defs>
      <path d="M0 112Q300 62 564 126V152Q290 92 0 146Z" fill="var(--grey-mid)"/>
      <path d="M0 122Q300 76 564 136V144Q300 84 0 130Z" fill="var(--blue-deep)"/>
      <path d="M0 146Q290 92 564 152V160Q290 100 0 154Z" fill="var(--blue-mid)"/>
      <path role="img" aria-label="Foto: Alpenkette im Dunst" d="M0 154Q290 100 564 160V442Q300 520 0 452Z" fill="url(#hazyRange)"/>
      <path d="M0 452Q300 520 564 442V730H0Z" fill="var(--blue-mid)"/>
      <path d="M0 452Q300 530 564 470V502Q320 540 0 452Z" fill="var(--grey-mid)"/>
      <path d="M0 452Q300 524 564 456V470Q300 532 0 452Z" fill="#a9c4e2"/>
      <path d="M0 452Q300 520 564 442" fill="none" stroke="var(--blue-deep)" stroke-width="6"/>
    </svg>
    <h1 class="cover-title cover-title--main serif">Geschäftsbericht Velnor AG</h1>
    <p class="cover-title cover-title--year serif">Geschäftsjahr2013</p>
    <p class="cover-claim sans">Bei Velnor investieren Unternehmer in mittelständische<br>Industrieunternehmen mit internationalem Entwicklungspotential</p>
  </section>
</div>
</body>
</html>
```